FREIGHT FORWARDING FLYER

We need a flyer designed for our company (Brightwell Freight Global) showing the list of services we offer to hand out to customers. Below is a list of services:<br/><br/>-Ocean/Air Import and Export<br/>-Exhibition Cargo<br/>-Carnet Application<br/>-Project Cargo (OOG/Flatrack/Reefer/DG)<br/>-Customs Clearance<br/>-Door to Door Services<br/>-Cargo Insurance<br/>-Warehousing<br/>-Trucking (LTL/FCL)

Target Market(s)

Customers who have a specific need for freight forwarding, especially customers at exhibitions.

Industry/Entity Type

Freight Forwarding

Colors

Designer to choose colors to be used in the design.

Requirements
Must have
• The services we offer need to pop to the customer and essentially get that interested in the services we offer.

```html
<!DOCTYPE html>
<html lang="en">
<head>
<meta charset="utf-8">
<title>Brightwell Freight Global – Services Flyer</title>
<link href="https://fonts.googleapis.com/css2?family=Arimo:wght@400;700&family=Tinos:wght@700&family=Roboto:wght@400;500&display=swap" rel="stylesheet">
<style>
  :root {
    --backdrop: #c8c1b6;
    --paper: #ffffff;
    --brand-red: #e3202b;
    --brand-blue: #1a8ccf;
    --icon-brown: #7a2a18;
    --ink: #1e1e1e;
    --ink-soft: #333333;
    --ink-grey: #6b6b6b;
    --divider: #444444;
  }
  * { box-sizing: border-box; margin: 0; padding: 0; }
  html, body { width: 900px; height: 1200px; overflow: hidden; }
  body { background: var(--backdrop); font-family: "Arimo", Arial, sans-serif; color: var(--ink); }

  .flyer { position: absolute; left: 85px; top: 82px; width: 732px; height: 1035px; background: var(--paper); box-shadow: 3px 4px 6px rgba(0,0,0,.35); }

  .brand-mark { position: absolute; left: 12px; top: 22px; width: 58px; height: 58px; background: var(--brand-red); }
  .brand-name { position: absolute; left: 177px; top: 20px; font-family: "Roboto", Arial, sans-serif; font-weight: 400; font-size: 17px; line-height: 20px; color: var(--ink-grey); letter-spacing: .4px; text-transform: uppercase; }

  .contact { position: absolute; left: 514px; top: 21px; font-family: "Roboto", Arial, sans-serif; font-weight: 500; font-size: 17px; color: var(--ink); }
  .contact li { list-style: none; display: flex; align-items: center; gap: 8px; height: 36px; }
  .contact svg { width: 17px; height: 17px; flex: none; }

  .hero { position: absolute; left: 0; top: 105px; width: 732px; height: 396px;
    background:
      radial-gradient(ellipse 260px 150px at 82% 66%, rgba(255,214,130,.95) 0%, rgba(248,196,110,.55) 45%, rgba(248,196,110,0) 100%),
      radial-gradient(ellipse 380px 220px at 40% 55%, rgba(222,190,110,.55) 0%, rgba(222,190,110,0) 100%),
      linear-gradient(180deg, #8db8da 0%, #b9cfdc 35%, #e9d2a4 62%, #e6b46c 76%, #8c6f52 88%, #5c4c44 100%); }

  .welcome { position: absolute; left: 15px; top: 516px; width: 702px; }
  .section-title { font-family: "Tinos", "Times New Roman", serif; font-weight: 700; font-size: 20px; color: var(--brand-blue); margin-bottom: 7px; }
  .welcome p { font-size: 12.2px; line-height: 19.3px; color: var(--ink-soft); }

  .services-title { position: absolute; left: 15px; top: 641px; }

  .divider { position: absolute; width: 0; border-left: 2px dotted var(--divider); }

  .service { position: absolute; width: 180px; text-align: center; }
  .service-icon { display: block; margin: 0 auto 8px; width: 46px; height: 50px; }
  .service h3 { font-family: "Tinos", "Times New Roman", serif; font-weight: 700; font-size: 16px; line-height: 18px; color: var(--ink); margin-bottom: 6px; }
  .service p { font-size: 9.6px; line-height: 13.6px; color: var(--ink-soft); }
  .service p + p { margin-top: 4px; }

  .footer-band { position: absolute; left: 0; bottom: 0; width: 732px; height: 14px; background: var(--brand-red); }
</style>
</head>
<body>
<main class="flyer">
  <header>
    <span class="brand-mark"></span>
    <span class="brand-name">Brightwell<br>Freight<br>Global</span>
    <ul class="contact">
      <li><svg viewBox="0 0 20 20"><path d="M4 2l4 1 1 4-2 2a11 11 0 0 0 4 4l2-2 4 1 1 4-2 2C9 18 2 11 2 4z" fill="none" stroke="var(--brand-red)" stroke-width="2"/></svg>555.014.2277</li>
      <li><svg viewBox="0 0 20 20"><circle cx="10" cy="10" r="8" fill="var(--brand-red)"/><path d="M2 10h16M10 2c-3 3-3 13 0 16M10 2c3 3 3 13 0 16" stroke="#fff" stroke-width="1.2" fill="none"/></svg>www.brightwellfg.com</li>
    </ul>
  </header>

  <div class="hero" role="img" aria-label="Photo of three cargo trucks driving in convoy along a highway at sunset"></div>

  <section class="welcome">
    <h2 class="section-title">Welcome to Brightwell Freight</h2>
    <p>Brightwell is a licensed Freight Forwarder company located in Harbor Point, NY, providing the entire spectrum of services: international shipping of containerized &amp; Ro/Ro cargo, loading, storage, trucking, forwarding, custom clearance etc. Over a decade of experience and contracts with some of the most reliable steamship lines ensures fast, trouble-free services to destinations all over the world at very competitive rates.</p>
  </section>

  <h2 class="section-title services-title">Our Services</h2>

  <span class="divider" style="left:231px; top:658px; height:185px;"></span>
  <span class="divider" style="left:492px; top:658px; height:185px;"></span>
  <span class="divider" style="left:231px; top:863px; height:150px;"></span>
  <span class="divider" style="left:492px; top:863px; height:150px;"></span>

  <article class="service" style="left:15px; top:682px;">
    <svg class="service-icon" viewBox="0 0 46 50"><ellipse cx="23" cy="25" rx="23" ry="25" fill="var(--icon-brown)"/><path d="M10 28h26l-4 7H14z M15 22h14v5H15z M19 17h5v5h-5z" fill="#fff"/></svg>
    <h3>Ocean Service</h3>
    <p>Ocean import &amp; export with no restrictions in the size &amp; weight of the cargo, door to door pick up, advance tracking technology &amp; managing shipping documents.</p>
  </article>

  <article class="service" style="left:267px; top:682px;">
    <svg class="service-icon" viewBox="0 0 46 50"><ellipse cx="23" cy="25" rx="23" ry="25" fill="var(--icon-brown)"/><path d="M33 14l-7 8 6 9-2 2-8-7-5 5 1 4-2 1-2-5-5-2 1-2 4 1 5-5-7-8 2-2 9 6 8-7z" fill="#fff"/></svg>
    <h3>Air Service</h3>
    <p>Brightwell provides a highly efficient network for all your international &amp; domestic Air Freight import &amp; export needs, delivering cargo across all major worldwide locations on very next day.</p>
  </article>

  <article class="service" style="left:535px; top:682px;">
    <svg class="service-icon" viewBox="0 0 46 50"><ellipse cx="23" cy="25" rx="23" ry="25" fill="var(--icon-brown)"/><path d="M9 17h18v13H9z M28 21h5l4 5v4h-9z" fill="#fff"/><circle cx="15" cy="32" r="2.5" fill="#fff"/><circle cx="31" cy="32" r="2.5" fill="#fff"/></svg>
    <h3>Trucking Service</h3>
    <p>Brightwell offers variety of customized &amp; cost-effective LTL &amp; FCL solutions for transportation by road. Your freight can be transported to any location in USA.</p>
  </article>

  <article class="service" style="left:15px; top:866px;">
    <svg class="service-icon" viewBox="0 0 46 50"><ellipse cx="23" cy="25" rx="23" ry="25" fill="var(--icon-brown)"/><path d="M23 12l13 12h-4v12H14V24h-4z" fill="#fff"/><rect x="20" y="28" width="6" height="8" fill="var(--icon-brown)"/></svg>
    <h3>Warehouse Service</h3>
    <p>Integrated WMS &amp; Warehousing Inventory/ Stock Management System</p>
    <p>Short-Term &amp; Long Term Storage</p>
    <p>CFS Approved &amp; Bonded Warehouse</p>
  </article>

  <article class="service" style="left:267px; top:866px;">
    <svg class="service-icon" viewBox="0 0 46 50"><ellipse cx="23" cy="25" rx="23" ry="25" fill="var(--icon-brown)"/><circle cx="15" cy="24" r="3.5" fill="#fff"/><circle cx="31" cy="24" r="3.5" fill="#fff"/><path d="M9 35c0-5 12-5 12 0z M25 35c0-5 12-5 12 0z M18 13h10v6h-6l-2 2v-2h-2z" fill="#fff"/></svg>
    <h3>Project Cargo</h3>
    <p>Out of gauge, Flatrack, Reefer &amp; DG shipments. Our team of experts will individually develop a suitable solution for every project.</p>
  </article>

  <article class="service" style="left:535px; top:866px;">
    <svg class="service-icon" viewBox="0 0 46 50"><ellipse cx="23" cy="25" rx="23" ry="25" fill="var(--icon-brown)"/><path d="M15 13h12l5 5v19H15z" fill="#fff"/><path d="M19 27l3 3 6-7" fill="none" stroke="var(--icon-brown)" stroke-width="2.4"/></svg>
    <h3>Exhibition &amp; Customs</h3>
    <p>Exhibition Cargo &amp; Carnet Application</p>
    <p>Customs Clearance</p>
    <p>Cargo Insurance &amp; Door to Door</p>
  </article>

  <div class="footer-band"></div>
</main>
</body>
</html>
```